Piano genealogy graphs template, for a large poster printing

Hello and thank you for your interest in my project.
I need a poster template, so I can create structures similar to the one I have uploaded. I want to completely replace or improve my poor previous design which is attached.
I need to be able to input names and dates into boxes of various colors, arrows pointing between boxes. I would also like to be able to label each graph (not each box).
I am looking at something that would be legible when printed, in a one consistent professional layout of 2A0 (around 1189x1682 mm) poster (I know it is large). The design template required here can include just few sample text boxes with sample flags on a suitable background, for me to multiply later and spread across the whole poster.
The positioning of the boxes is not important.
Please let me know if more clarification is required.
Thank you for your help.

Feel free to follow what I have attached in the file, or change the design completely.

UPDATE 4/12: I have uploaded two more graphs as an example. At this stage of the contest, I would like to have one of those graphs done, and I am planning to offer a 'freelance job' to one or two designers, who will be willing to do the whole 10 graphs on one poster.

Reason: Dear Designers, Since the project is rather complex and large-scale, I have decided to give everyone more time to work on their designs. I will consider extending it further if any of you require additional time. Best wishes, leopold

Dear Designers, I would like to inform you that the contest for my poster is now closed and that I have assigned the prizes. I would like to thank all of you for submiting your high-quality designs, and for your participation. It was a great pleasure working with all of you. Due to the large size of the project itself (large number of graphs to be fitted on a single poster), I had to focus on providing feedback to only those designers who provided projects closest to what I was expecting at the early stages of the contest. I wish you all the best for the future, Kind regards, Leopold

Target Market(s)

Pianists, historians

Industry/Entity Type

Printing

Requirements
Must have
• Consistent design, but allow to clearly delineate various genealogy trees.

```html
<!DOCTYPE html>
<html lang="en">
<head>
<meta charset="utf-8">
<title>Genealogical Trees of Pianists – American Tree, Branch II</title>
<link href="https://fonts.googleapis.com/css2?family=Pathway+Gothic+One&display=swap" rel="stylesheet">
<style>
  :root {
    --bg-top: #1c1c1c;
    --bg-mid: #0e0e0e;
    --bg-deep: #050505;
    --ink: #f2f2f2;
    --ink-soft: #d9d9d9;
    --line: #9a9a9a;
    --flourish: #7a7a7a;
    --it-green: #1f9a48;
    --it-white: #f4f4f4;
    --it-red: #d9262e;
    --key-light: #e6e6e6;
    --key-shadow: #2a2a2a;
  }
  * { box-sizing: border-box; margin: 0; padding: 0; }
  html, body { width: 848px; height: 1200px; overflow: hidden; background: var(--bg-deep); }
  .poster {
    position: relative; width: 848px; height: 1200px; overflow: hidden;
    background: radial-gradient(ellipse at 50% 25%, var(--bg-top) 0%, var(--bg-mid) 55%, var(--bg-deep) 100%);
    font-family: "Pathway Gothic One", "Arial Narrow", sans-serif;
    font-weight: 400;
    color: var(--ink);
  }
  .title-ornament {
    position: absolute; left: 198px; top: 14px; width: 498px; height: 176px;
    background: radial-gradient(ellipse at center, rgba(120,120,120,0.28) 0%, rgba(60,60,60,0.12) 55%, rgba(0,0,0,0) 75%);
  }
  .title {
    position: absolute; left: 0; top: 0; width: 848px; height: 170px;
    font-family: "Pathway Gothic One", "Arial Narrow", sans-serif;
    font-weight: 400; color: var(--ink);
  }
  .title-small { position: absolute; left: 330px; top: 52px; font-size: 36px; line-height: 1; white-space: nowrap; letter-spacing: 1px; }
  .title-large { position: absolute; left: 206px; top: 80px; font-size: 80px; line-height: 1; white-space: nowrap; letter-spacing: 3px; }
  .graph-label {
    position: absolute; left: 0; width: 848px; top: 212px; text-align: center;
    font-size: 32px; line-height: 36px; font-weight: 400; letter-spacing: 0.3px; color: var(--ink);
  }
  .flag-bar {
    position: absolute; left: 461px; top: 252px; width: 169px; height: 8px; display: flex;
  }
  .flag-bar span { flex: 1; }
  .flag-bar .green { background: var(--it-green); }
  .flag-bar .white { background: var(--it-white); }
  .flag-bar .red { background: var(--it-red); }
  .connectors { position: absolute; left: 0; top: 0; width: 848px; height: 900px; }
  .entry {
    position: absolute; text-align: center; font-size: 13.5px; line-height: 15px;
    color: var(--ink-soft); white-space: nowrap; transform: translateX(-50%);
  }
  .flourish {
    position: absolute; background: var(--flourish); opacity: 0.55; border-radius: 6px;
  }
  .flourish.top, .flourish.bottom { width: 36px; height: 8px; left: 50%; margin-left: -18px; }
  .flourish.top { top: -18px; }
  .flourish.bottom { bottom: -18px; }
  .flourish.left, .flourish.right { width: 12px; height: 34px; top: 50%; margin-top: -17px; }
  .flourish.left { left: -20px; }
  .flourish.right { right: -20px; }
  .keyboard {
    position: absolute; left: 0; top: 864px; width: 848px; height: 336px;
    background: linear-gradient(180deg, var(--bg-deep) 0%, var(--key-shadow) 18%, #bdbdbd 45%, var(--key-light) 70%, #8c8c8c 88%, #1a1a1a 100%);
  }
</style>
</head>
<body>
<main class="poster">
  <div class="title-ornament" role="img" aria-label="Faint baroque scroll ornament behind the title"></div>
  <h1 class="title">
    <span class="title-small">Genealogical Trees of</span>
    <span class="title-large">Pianists</span>
  </h1>

  <h2 class="graph-label">American Tree, Branch II - Italian influences</h2>
  <div class="flag-bar" aria-hidden="true"><span class="green"></span><span class="white"></span><span class="red"></span></div>

  <svg class="connectors" viewBox="0 0 848 900" aria-hidden="true" fill="none" stroke="var(--line)" stroke-width="1.4">
    <path d="M300 372 C 420 372, 442 385, 442 422"/>
    <path d="M528 472 C 640 472, 666 490, 666 520"/>
    <path d="M666 610 C 666 655, 610 668, 528 668"/>
    <path d="M440 708 C 440 745, 400 762, 300 762"/>
    <line x1="210" y1="448" x2="210" y2="492"/>
    <line x1="198" y1="470" x2="222" y2="470" stroke-width="1"/>
    <line x1="210" y1="642" x2="210" y2="686"/>
    <line x1="198" y1="664" x2="222" y2="664" stroke-width="1"/>
  </svg>

  <div class="entry" style="left:210px; top:308px;">
    <span class="flourish top" role="img" aria-label="Scroll ornament"></span>
    <span class="flourish left" role="img" aria-label="Scroll ornament"></span>
    <span class="flourish right" role="img" aria-label="Scroll ornament"></span>
    <span class="flourish bottom" role="img" aria-label="Scroll ornament"></span>
    - Lorem ipsum dolor sit amet,<br>- Consectetur adipiscing elit.<br>-Duis ac efficitur augue. Donec<br>-Quis turpis a elit iaculis<br>- Mollis. Nunc sed malesuada<br>- Curabitur sed sagittis dolor.<br>- Nam blandit nunc eget nisi
  </div>

  <div class="entry" style="left:210px; top:505px;">
    <span class="flourish left" role="img" aria-label="Scroll ornament"></span>
    <span class="flourish right" role="img" aria-label="Scroll ornament"></span>
    - Lorem ipsum dolor sit amet,<br>- Consectetur adipiscing elit.<br>-Duis ac efficitur augue. Donec<br>-Quis turpis a elit iaculis<br>- Mollis. Nunc sed malesuada<br>- Curabitur sed sagittis dolor.<br>- Nam blandit nunc eget nisi
  </div>

  <div class="entry" style="left:210px; top:700px;">
    <span class="flourish left" role="img" aria-label="Scroll ornament"></span>
    <span class="flourish right" role="img" aria-label="Scroll ornament"></span>
    <span class="flourish bottom" role="img" aria-label="Scroll ornament"></span>
    - Lorem ipsum dolor sit amet,<br>- Consectetur adipiscing elit.<br>-Duis ac efficitur augue. Donec<br>-Quis turpis a elit iaculis<br>- Mollis. Nunc sed malesuada<br>- Curabitur sed sagittis dolor.<br>- Nam blandit nunc eget nisi
  </div>

  <div class="entry" style="left:442px; top:436px;">
    <span class="flourish left" role="img" aria-label="Scroll ornament"></span>
    <span class="flourish right" role="img" aria-label="Scroll ornament"></span>
    <span class="flourish bottom" role="img" aria-label="Scroll ornament"></span>
    - Lorem ipsum dolor sit amet,<br>- Consectetur adipiscing elit.<br>- Mollis. Nunc sed malesuada<br>- Curabitur sed sagittis dolor.
  </div>

  <div class="entry" style="left:666px; top:530px;">
    <span class="flourish left" role="img" aria-label="Scroll ornament"></span>
    <span class="flourish right" role="img" aria-label="Scroll ornament"></span>
    - Lorem ipsum dolor sit amet,<br>- Consectetur adipiscing elit.<br>- Mollis. Nunc sed malesuada<br>- Curabitur sed sagittis dolor.
  </div>

  <div class="entry" style="left:442px; top:634px;">
    <span class="flourish top" role="img" aria-label="Scroll ornament"></span>
    <span class="flourish left" role="img" aria-label="Scroll ornament"></span>
    <span class="flourish right" role="img" aria-label="Scroll ornament"></span>
    - Lorem ipsum dolor sit amet,<br>- Consectetur adipiscing elit.<br>- Mollis. Nunc sed malesuada<br>- Curabitur sed sagittis dolor.
  </div>

  <div class="keyboard" role="img" aria-label="Close-up photograph of piano keys, black and white keys receding into darkness"></div>
</main>
</body>
</html>
```